BSWC Steadwell Foot Health Care

Steadwell Foot Health Care guarantees to treat your foot problems in one visit or we will provide a free treatment session to you until you are completely satisfied.

10% discount for all new patients!

Mobile foot care at home!

Professional and fully qualified and insured foot health care practitioner

Expert advice

How to care for your feet

Treatments; Diabetic foot health, Corns, Callouses, Fungal Infections, Verrucas, Cracked Heels, Ingrowing Toenails, Ball of foot pain and Heel pain.

```html
<!DOCTYPE html>
<html lang="en">
<head>
<meta charset="utf-8">
<title>BSWC Steadwell Foot Health Care – Flyer</title>
<link rel="stylesheet" href="https://fonts.googleapis.com/css2?family=Oswald:wght@300;400&family=Source+Sans+3:wght@400;600&display=swap">
<style>
  :root {
    --teal: #6fb9bb;
    --teal-deep: #1a9d8c;
    --teal-text: #3fa7a6;
    --yellow: #e2db8c;
    --yellow-text: #e3d35a;
    --grey: #7d7e80;
    --grey-text: #68696b;
    --paper: #ffffff;
    --backdrop: #eceae6;
  }
  * { box-sizing: border-box; margin: 0; padding: 0; }
  html, body { width: 1200px; height: 878px; overflow: hidden; background: var(--backdrop); }
  body { position: relative; font-family: "Source Sans 3", Arial, sans-serif; }

  .flyer {
    position: absolute; width: 466px; height: 658px;
    background: var(--paper); overflow: hidden;
    box-shadow: 0 3px 10px rgba(0,0,0,.25);
  }
  .flyer--front { left: 76px; top: 87px; }
  .flyer--back { left: 620px; top: 136px; }

  .dot { position: absolute; border-radius: 50%; }
  .dot--teal { background: var(--teal); }
  .dot--deep { background: var(--teal-deep); }
  .dot--yellow { background: var(--yellow); }
  .dot--grey { background: var(--grey); }
  .dot--white { background: var(--paper); }
  .dot--blend { mix-blend-mode: multiply; opacity: .9; }

  .abs { position: absolute; }
  .condensed { font-family: "Oswald", "Arial Narrow", sans-serif; font-weight: 300; }

  /* front */
  .hero-photo {
    left: 0; top: 0; width: 466px; height: 245px;
    background: linear-gradient(160deg, #f6e3d6 0%, #efc9b3 45%, #f8efe9 80%, #fff 100%);
  }
  .offer-badge {
    color: #fff; font-size: 25px; line-height: 27px; text-align: center;
    left: 311px; top: 29px; width: 142px;
  }
  .headline {
    left: 0; width: 466px; top: 259px; text-align: center;
    color: var(--grey-text); font-weight: 600; font-size: 24px; letter-spacing: .3px;
  }
  .rule { position: absolute; height: 2px; background: var(--teal-deep); }
  .brand-line {
    left: 0; width: 466px; top: 301px; text-align: center;
    color: var(--teal-text); font-weight: 600; font-size: 16.5px;
  }
  .promise { left: 19px; top: 424px; width: 200px; color: #fff; font-size: 12px; line-height: 15px; }
  .promise h2 { font-size: 12.5px; font-weight: 600; padding-bottom: 4px; border-bottom: 2px solid var(--teal-deep); margin-bottom: 5px; }
  .promise .perk { color: var(--yellow-text); margin-top: 14px; }

  .treatments { left: 265px; top: 396px; width: 200px; color: var(--teal-text); font-size: 12px; line-height: 15.5px; }
  .treatments h2 { font-size: 12.5px; font-weight: 600; color: var(--teal-deep); width: 120px; padding-bottom: 2px; border-bottom: 2px solid var(--yellow-text); margin-bottom: 6px; }

  .call { color: var(--grey-text); font-size: 24px; left: 265px; top: 513px; }
  .phone { display: flex; align-items: center; gap: 8px; color: var(--teal-deep); font-family: "Source Sans 3", Arial, sans-serif; font-weight: 600; font-size: 24px; letter-spacing: .5px; }
  .phone svg { flex: none; }
  .front-phone { left: 265px; top: 552px; }

  .accreditation { left: 289px; top: 604px; display: flex; gap: 8px; align-items: center; }
  .accreditation .badge-a { width: 52px; height: 20px; background: #6b3d8f; border-radius: 2px; }
  .accreditation .badge-b { width: 32px; height: 34px; background: #2f5a3a; }

  /* back */
  .intro { left: 13px; top: 66px; width: 172px; color: #fff; font-size: 11.5px; line-height: 14.5px; }
  .intro-offer { left: 13px; top: 127px; color: var(--yellow-text); font-size: 15px; font-weight: 400; white-space: nowrap; }
  .back-call { left: 13px; top: 171px; color: var(--yellow-text); font-size: 16.5px; font-weight: 400; }
  .back-phone { left: 16px; top: 197px; color: var(--yellow-text); font-size: 18px; gap: 6px; }

  .pledge { left: 238px; top: 31px; width: 218px; text-align: right; color: var(--teal-text); font-size: 11.5px; line-height: 15.5px; }
  .pledge h2 { text-align: left; font-size: 12.5px; font-weight: 600; color: var(--yellow-text); padding-left: 16px; padding-bottom: 3px; border-bottom: 2px solid var(--teal-deep); margin-bottom: 7px; white-space: nowrap; }
  .pledge p + p { margin-top: 15px; }
  .pledge .accent { color: var(--yellow-text); }

  .specialism { left: 48px; top: 318px; width: 386px; text-align: center; color: var(--grey-text); font-size: 12px; line-height: 16px; }
  .specialism .accent { color: var(--teal-text); }

  .photo-ring { position: absolute; width: 136px; height: 136px; border-radius: 50%; border: 3px solid var(--teal); padding: 4px; top: 403px; }
  .photo-ring .photo { width: 100%; height: 100%; border-radius: 50%; }
  .photo--one { background: radial-gradient(circle at 45% 55%, #e8d3c4, #b48c7a 60%, #5c4840); }
  .photo--two { background: radial-gradient(circle at 50% 50%, #f0e0cf, #cfa98e 55%, #8d8f93); }
  .photo--three { background: radial-gradient(circle at 55% 50%, #d9b7a8, #a8423e 55%, #3b3233); }

  .visit { left: 0; width: 466px; top: 556px; text-align: center; color: var(--teal-deep); font-size: 16.5px; line-height: 22px; }
</style>
</head>
<body>

<section class="flyer flyer--front" aria-label="Front of flyer">
  <div class="abs hero-photo" role="img" aria-label="Photo of pampered feet with white daisies between the toes"></div>
  <div class="dot dot--yellow" style="left:444px;top:-4px;width:30px;height:30px"></div>
  <div class="dot dot--teal" style="left:311px;top:5px;width:142px;height:142px;opacity:.92"></div>
  <p class="abs offer-badge condensed">10% off<br>for all new<br>patients!</p>

  <h1 class="abs headline">MOBILE FOOT CARE AT HOME!</h1>
  <div class="rule" style="left:33px;top:292px;width:398px"></div>
  <p class="abs brand-line">BSWC Steadwell Foot Health Care</p>

  <div class="dot dot--yellow" style="left:-32px;top:295px;width:130px;height:130px"></div>
  <div class="dot dot--teal" style="left:401px;top:300px;width:76px;height:76px"></div>
  <div class="dot dot--teal" style="left:-5px;top:344px;width:294px;height:294px"></div>
  <div class="dot dot--deep" style="left:197px;top:567px;width:130px;height:130px"></div>
  <div class="dot dot--yellow" style="left:212px;top:343px;width:164px;height:164px"></div>
  <div class="dot dot--white" style="left:229px;top:370px;width:306px;height:306px"></div>
  <div class="dot dot--grey" style="left:403px;top:599px;width:88px;height:88px"></div>

  <div class="abs promise">
    <h2>BSWC Steadwell Foot Health Care</h2>
    <p>Steadwell Foot Health Care guarantees to treat your foot problems in one visit or we will provide a free treatment session to you until you are completely satisfied.</p>
    <p class="perk">Professional and fully qualified and insured foot health care practitioner</p>
    <p class="perk">Expert advice</p>
    <p class="perk">How to care for your feet</p>
  </div>

  <div class="abs treatments">
    <h2>TREATMENTS</h2>
    <p>Diabetic foot health, Corns, Callouses, Fungal Infections, Verrucas, Cracked Heels, Ingrowing Toenails, Ball of foot pain and Heel pain.</p>
  </div>

  <p class="abs call condensed">CALL NOW to register</p>
  <p class="abs phone front-phone">
    <svg width="24" height="24" viewBox="0 0 24 24" aria-hidden="true"><circle cx="12" cy="12" r="10.5" fill="none" stroke="currentColor" stroke-width="2"/><path d="M8.6 6.8l1.7-.3 1 2.6-1.1.9c.6 1.4 1.6 2.4 3 3l.9-1.1 2.6 1-.3 1.7c-.2.6-.8 1-1.4.9-3.6-.5-6.4-3.3-6.9-6.9-.1-.6.3-1.2.5-1.8z" fill="currentColor"/></svg>
    07700900412
  </p>

  <div class="abs accreditation" aria-label="Accreditation badges">
    <div class="badge-a"></div>
    <div class="badge-b"></div>
  </div>
</section>

<section class="flyer flyer--back" aria-label="Back of flyer">
  <div class="dot dot--teal" style="left:-10px;top:10px;width:246px;height:246px"></div>
  <div class="dot dot--grey dot--blend" style="left:146px;top:-14px;width:104px;height:104px"></div>
  <div class="dot dot--yellow dot--blend" style="left:-76px;top:190px;width:140px;height:140px"></div>
  <div class="dot dot--teal" style="left:372px;top:293px;width:104px;height:104px"></div>
  <div class="dot dot--yellow" style="left:381px;top:597px;width:60px;height:60px"></div>
  <div class="dot dot--grey dot--blend" style="left:404px;top:598px;width:70px;height:70px"></div>

  <p class="abs intro">NEWLY ARRIVED MOBILE FOOT CARE AT HOME IS IN NOW AVAILABLE IN YOUR AREA</p>
  <p class="abs intro-offer condensed">10% Discounts for all new patients</p>
  <p class="abs back-call condensed">CALL NOW to register</p>
  <p class="abs phone back-phone">
    <svg width="19" height="19" viewBox="0 0 24 24" aria-hidden="true"><circle cx="12" cy="12" r="10.5" fill="none" stroke="currentColor" stroke-width="2"/><path d="M8.6 6.8l1.7-.3 1 2.6-1.1.9c.6 1.4 1.6 2.4 3 3l.9-1.1 2.6 1-.3 1.7c-.2.6-.8 1-1.4.9-3.6-.5-6.4-3.3-6.9-6.9-.1-.6.3-1.2.5-1.8z" fill="currentColor"/></svg>
    07700900412
  </p>

  <div class="abs pledge">
    <h2>BSWC Steadwell Foot Health Care</h2>
    <p>Guarantees to treat your foot problems in one visit or we will provide a free treatment session to you until you're completely satisfied.</p>
    <p>From as little as 30 per treatment session our fully qualified and insured Foot Health Care Practitioner will immediately bring you pain relief while also offering you professional expert advice on how to care for your feet and <span class="accent">KEEP THEM LOOKING GOOD ALL YEAR ROUND.</span></p>
  </div>

  <p class="abs specialism">Specialising in Diabetic foot health and Elderly foot care<br><span class="accent">10% off TREATMENTS</span> Corns, Calluses, Fungal infections, Verruca's, Cracked heels, In growing toenails, Ball of foot pain, Heel pain and Diabetic Foot Health.</p>

  <div class="photo-ring" style="left:14px"><div class="photo photo--one" role="img" aria-label="Photo of a practitioner treating toes with an instrument"></div></div>
  <div class="photo-ring" style="left:164px"><div class="photo photo--two" role="img" aria-label="Photo of gloved hands treating the sole of a foot"></div></div>
  <div class="photo-ring" style="left:312px"><div class="photo photo--three" role="img" aria-label="Photo of a foot treatment session at home"></div></div>

  <p class="abs visit">We will conveniently visit you in your own home or<br>place of work which ever you find more comfortable.</p>
</section>

</body>
</html>
```